Lumora Works - Design & Marketing Website Re-branding

UPDATE:
We are working on finalizing our color palette but are hoping that the designers will guide us to the right choice of colors by looking at our color inspiration file that we just uploaded and lead us in the right direction.

-----

I am exploring new design inspiration for a re-branding of my website. My current website is old and outdated and I lack the time to design it myself in addition to the fact that I am my own worst client.

I do website design, development and marketing as well as some SEO consulting and business development for small to mid-size companies in a range of industries.

https://lumoraworks.example

I like clean modern designs without cartoon images. The brands I'm going after are looking for a professional look and feel. I need something that shows my many years of being in business that is very professional.

I prefer minimal use of color. Mostly black and white with maybe one or two other colors. I am open to the suggestions by the designer.

Target Market(s)

Small to mid-size companies

Industry/Entity Type

Website Design, SEO and Markeitng

Number of Pages Required

4 page

Font styles to use
Sans Serif

Requirements
Must have
• Must be clean, modern and professional - I am not a huge fan of a lot of color and I'm open to new color suggestions by the designer
Nice to have
• A good balance of whitespace to content and graphics
Should not have
• Please no people illustrations

```html
<!DOCTYPE html>
<html lang="en">
<head>
<meta charset="utf-8">
<title>Lumora Works — Web Design, Development &amp; Marketing</title>
<link href="https://fonts.googleapis.com/css2?family=Kumbh+Sans:wght@400;500;600;700;800&display=swap" rel="stylesheet">
<style>
  :root{
    --navy:#1b2236;
    --navy-deep:#121829;
    --blue:#2f66e8;
    --blue-light:#4f8ff8;
    --ink:#1a1f2e;
    --white:#ffffff;
    --grey-text:#3c4254;
    --label-bg:#3a4153;
  }
  *{box-sizing:border-box;margin:0;padding:0}
  html,body{width:1200px;height:3228px;overflow:hidden}
  body{position:relative;background:var(--white);font-family:"Kumbh Sans",Arial,sans-serif;color:var(--ink)}
  .abs{position:absolute}

  /* Hero */
  .hero{left:0;top:0;width:1200px;height:750px;
    background:radial-gradient(ellipse at 30% 20%,#5a4a36 0%,#2a2520 30%,#121212 70%),#111;}
  .hero-shade{left:0;top:0;width:1200px;height:750px;background:linear-gradient(180deg,rgba(0,0,0,.15),rgba(0,0,0,.45))}
  .nav{left:142px;top:0;width:914px;height:80px;background:var(--navy);display:flex;align-items:center}
  .brand{width:150px;height:80px;display:flex;align-items:center;gap:10px;padding-left:18px;background:var(--white)}
  .brand-dot{width:16px;height:16px;border-radius:50%;background:var(--blue)}
  .brand-name{font-weight:700;font-size:17px;color:var(--navy);line-height:1.05}
  .nav-links{display:flex;gap:0;margin-left:55px;list-style:none}
  .nav-links li{color:var(--white);font-size:15px;font-weight:500;width:112px}
  .hero-label{left:0;width:1200px;top:268px;display:flex;justify-content:center;gap:16px;align-items:center}
  .hero-label span{background:var(--white);color:var(--navy);font-weight:700;font-size:15px;letter-spacing:1px;padding:3px 10px}
  .hero-label i{color:var(--white);font-style:normal;font-weight:700;letter-spacing:3px}
  .hero-title{left:0;width:1200px;top:300px;text-align:center;color:var(--white);font-weight:700;font-size:58px;line-height:1.08}
  .hero-sub{left:0;width:1200px;top:428px;text-align:center;color:var(--white);font-size:16px;line-height:1.45;font-weight:500}
  .btn{display:flex;align-items:center;justify-content:center;gap:16px;color:var(--white);font-weight:700;font-size:15px;
    background:linear-gradient(90deg,var(--blue),var(--blue-light))}
  .hero-btn{left:517px;top:503px;width:166px;height:46px}

  /* Section labels & titles */
  .label{background:var(--label-bg);color:var(--white);font-size:14px;letter-spacing:1px;padding:4px 24px;font-weight:500}
  .section-title{font-weight:700;font-size:50px;line-height:1.12;color:var(--navy)}

  .services-bg{left:0;top:750px;width:1200px;height:597px;background:linear-gradient(160deg,#ffffff 0%,#eef0f4 45%,#ffffff 100%)}
  .card{top:1039px;width:291px;height:203px;background:var(--navy);color:var(--white);padding:0 22px}
  .card-icon{position:absolute;left:42px;top:18px;width:42px;height:42px;background:var(--blue)}
  .card-arrow{position:absolute;right:38px;top:28px;width:26px;height:18px;background:var(--blue);display:flex;align-items:center;justify-content:center}
  .card h3{position:absolute;left:42px;top:78px;font-size:20px;font-weight:700}
  .card p{position:absolute;left:42px;top:112px;width:210px;font-size:13px;line-height:1.4}

  /* Testimonial */
  .testimonial-bg{left:0;top:1347px;width:1200px;height:334px;background:radial-gradient(ellipse at 80% 40%,#4a3a2e 0%,#221d1b 45%,#141313 100%)}
  .quote-box{left:208px;top:1442px;width:781px;height:141px;border:1.5px solid #e8e8e8;border-bottom:none}
  .quote-line-l,.quote-line-r{top:1583px;height:1.5px;background:#e8e8e8}
  .avatar{left:355px;top:1458px;width:112px;height:112px;border-radius:50%;background:radial-gradient(circle at 50% 40%,#d8d8d8,#9a9a9a)}
  .quote-text{left:514px;top:1484px;width:310px;color:var(--white);font-size:14px;line-height:1.45}
  .quote-author{left:555px;top:1572px;color:var(--white);font-weight:700;font-size:15px;letter-spacing:1px}
  .quote-mark{left:868px;top:1420px;color:var(--white);font-weight:800;font-size:110px;line-height:1;background:#1c1917;padding:0 6px}
  .quote-nav{left:890px;top:1540px;display:flex;gap:16px}

  /* About */
  .about-title{left:142px;top:1818px}
  .about-text{left:142px;width:420px;font-size:13.5px;line-height:1.5;color:var(--ink)}
  .about-photo{left:766px;top:1788px;width:290px;height:290px;border-radius:50%;background:radial-gradient(circle at 45% 40%,#4b5a5c 0%,#2b3536 55%,#182020 100%)}
  .feature{top:2139px;height:97px;background:var(--navy);color:var(--white)}
  .feature h3{position:absolute;top:10px;left:0;width:100%;text-align:center;font-size:19px;font-weight:700}
  .feature-icon{position:absolute;left:14px;top:48px}
  .feature p{position:absolute;left:62px;top:42px;font-size:12px;line-height:1.4;width:calc(100% - 74px)}

  /* CTA */
  .cta-bg{left:0;top:2334px;width:1200px;height:430px;background:linear-gradient(180deg,#3b4150 0%,#2c3240 100%)}
  .cta-label{left:0;width:1200px;top:2447px;display:flex;justify-content:center}
  .cta-label span{background:#dfe1e6;color:var(--navy);font-size:14px;padding:3px 16px;letter-spacing:.5px}
  .cta-title{left:0;width:1200px;top:2480px;text-align:center;color:var(--white);font-weight:700;font-size:46px;line-height:1.2}
  .cta-btn{left:517px;top:2617px;width:166px;height:48px}

  /* Footer */
  .footer-bg{left:0;top:2764px;width:1200px;height:464px;background:linear-gradient(180deg,#f6f7f9,#ffffff)}
  .footer-brand{left:142px;top:2900px;display:flex;align-items:center;gap:18px}
  .footer-brand .brand-dot{width:40px;height:40px}
  .footer-brand span{font-size:52px;font-weight:700;color:var(--navy);line-height:1}
  .footer-tagline{left:142px;top:3021px;width:294px;height:22px;background:var(--label-bg);color:var(--white);font-size:14px;display:flex;align-items:center;justify-content:center;letter-spacing:.5px}
  .footer-email{left:142px;top:3060px;font-weight:700;font-size:38px;color:var(--navy)}
  .copyright{left:142px;top:3116px;font-size:13px}
  .copyright b{font-weight:700}
  .footer-col{top:2862px}
  .footer-col h4{font-size:19px;font-weight:700;color:var(--navy);margin-bottom:12px}
  .footer-col li{list-style:none;font-size:13px;line-height:30px;color:var(--ink)}
  .social{left:948px;top:3069px;display:flex;gap:9px}
  .social span{width:22px;height:22px;border-radius:50%;background:#2f3a3f}
</style>
</head>
<body>

<!-- Hero -->
<div class="abs hero" role="img" aria-label="Photo of a man with glasses working at a laptop in a dim office"></div>
<div class="abs hero-shade"></div>
<header class="abs nav">
  <div class="brand"><span class="brand-dot"></span><span class="brand-name">Lumora<br>Works</span></div>
  <ul class="nav-links"><li>Home</li><li>About Us</li><li>Services</li><li>Blogs</li><li>Contact</li></ul>
</header>
<div class="abs hero-label"><span>LUMORA WORKS</span><i>...</i><span>WELCOME</span></div>
<h1 class="abs hero-title">EVERY BUSINESS HAS<br>A STORY</h1>
<p class="abs hero-sub">Compelling website experiences that elevate<br>your business.</p>
<a class="abs btn hero-btn">What We DO
  <svg width="12" height="8" viewBox="0 0 12 8"><path d="M1 1l5 5 5-5" stroke="#fff" stroke-width="2" fill="none"/></svg></a>

<!-- Services -->
<div class="abs services-bg" role="img" aria-label="Soft grey flowing dotted wave backdrop"></div>
<div class="abs label" style="left:142px;top:850px">WHAT WE'RE OFFERING</div>
<h2 class="abs section-title" style="left:142px;top:884px">SERVICES WE'RE PROVIDING<br>TO OUR CUSTOMERS</h2>

<article class="abs card" style="left:142px">
  <span class="card-icon"></span>
  <span class="card-arrow"><svg width="12" height="8" viewBox="0 0 12 8"><path d="M1 4h9M7 1l3 3-3 3" stroke="#fff" stroke-width="1.5" fill="none"/></svg></span>
  <h3>Websites Simplified</h3>
  <p>A complete end-to-end website subscription solution that propels your business forward.</p>
</article>
<article class="abs card" style="left:453px">
  <span class="card-icon"></span>
  <span class="card-arrow"><svg width="12" height="8" viewBox="0 0 12 8"><path d="M1 4h9M7 1l3 3-3 3" stroke="#fff" stroke-width="1.5" fill="none"/></svg></span>
  <h3>Custom Website Design</h3>
  <p>A complete end-to-end website subscription solution that propels your business forward.</p>
</article>
<article class="abs card" style="left:767px">
  <span class="card-icon"></span>
  <span class="card-arrow"><svg width="12" height="8" viewBox="0 0 12 8"><path d="M1 4h9M7 1l3 3-3 3" stroke="#fff" stroke-width="1.5" fill="none"/></svg></span>
  <h3>Websites Support</h3>
  <p>A complete end-to-end website subscription solution that propels your business forward.</p>
</article>

<!-- Testimonial -->
<div class="abs testimonial-bg" role="img" aria-label="Dim photo of a team meeting around a table"></div>
<div class="abs quote-box"></div>
<div class="abs quote-line-l" style="left:208px;width:335px"></div>
<div class="abs quote-line-r" style="left:690px;width:299px"></div>
<div class="abs avatar" role="img" aria-label="Client portrait"></div>
<p class="abs quote-text">Lumora Works provided us with a high quality, functional, easy to navigate and beautiful website.</p>
<div class="abs quote-author">- R. DELANE</div>
<div class="abs quote-mark">&rdquo;</div>
<div class="abs quote-nav">
  <svg width="20" height="10" viewBox="0 0 20 10"><path d="M19 5H2M6 1L2 5l4 4" stroke="#fff" stroke-width="1.5" fill="none"/></svg>
  <svg width="20" height="10" viewBox="0 0 20 10"><path d="M1 5h17M14 1l4 4-4 4" stroke="#fff" stroke-width="1.5" fill="none"/></svg>
</div>

<!-- About -->
<div class="abs label" style="left:142px;top:1785px">About The Agency</div>
<h2 class="abs section-title about-title">WE CREATE WEBSITES<br>THAT INSPIRE</h2>
<p class="abs about-text" style="top:1938px">We are a collaborative team of word nerds, choreographers of shapes &amp; ideas, embassadors of data, content warriors and inspirational conversationalists ready to help you no matter where you are in your journey.</p>
<p class="abs about-text" style="top:2018px">We have a deep understanding of what it takes to grow a business and we collaborate with you every step of the way from strategy to implementation and beyond.</p>
<div class="abs about-photo" role="img" aria-label="Photo of a small team reviewing work on a laptop"></div>

<div class="abs feature" style="left:142px;width:253px">
  <h3>Proven Process</h3>
  <svg class="feature-icon" width="34" height="30" viewBox="0 0 34 30"><rect x="1" y="1" width="32" height="22" rx="2" stroke="#4f8ff8" stroke-width="2" fill="none"/><path d="M12 29h10M17 23v6" stroke="#4f8ff8" stroke-width="2"/></svg>
  <p>We have carefully crafted each step in our process for successful outcomes.</p>
</div>
<div class="abs feature" style="left:458px;width:250px">
  <h3>Connection</h3>
  <svg class="feature-icon" width="34" height="30" viewBox="0 0 34 30"><circle cx="10" cy="15" r="7" stroke="#4f8ff8" stroke-width="2" fill="none"/><circle cx="24" cy="15" r="7" stroke="#4f8ff8" stroke-width="2" fill="none"/></svg>
  <p>We take the time to truly listen and understand your audience and business needs.</p>
</div>
<div class="abs feature" style="left:770px;width:289px">
  <h3>Exceeding Your Goals</h3>
  <svg class="feature-icon" width="34" height="30" viewBox="0 0 34 30"><circle cx="17" cy="15" r="13" stroke="#4f8ff8" stroke-width="2" fill="none"/><circle cx="17" cy="15" r="6" stroke="#4f8ff8" stroke-width="2" fill="none"/></svg>
  <p>We develop actionable strategies for success based on your unique goals.</p>
</div>

<!-- CTA -->
<div class="abs cta-bg" role="img" aria-label="Muted photo of colleagues working together at a desk"></div>
<div class="abs cta-label"><span>Have Any Project In Mind?</span></div>
<h2 class="abs cta-title">GET IN TOUCH WITH<br>US!</h2>
<a class="abs btn cta-btn">Get Started
  <svg width="12" height="8" viewBox="0 0 12 8"><path d="M1 1l5 5 5-5" stroke="#fff" stroke-width="2" fill="none"/></svg></a>

<!-- Footer -->
<div class="abs footer-bg" role="img" aria-label="Light backdrop of flowing contour lines"></div>
<div class="abs footer-brand"><span class="brand-dot"></span><span>Lumora Works</span></div>
<div class="abs footer-tagline">Let's Start Working Together</div>
<div class="abs footer-email">Hello@LumoraWorks.Example</div>
<p class="abs copyright">© Copyright 2024 by <b>lumora works</b></p>
<nav class="abs footer-col" style="left:711px">
  <h4>Quick Links</h4>
  <ul><li>Home</li><li>About Us</li><li>Services</li><li>Blogs</li><li>Contact</li></ul>
</nav>
<nav class="abs footer-col" style="left:894px">
  <h4>Privacy</h4>
  <ul><li>Terms</li><li>Disclaimer</li></ul>
</nav>
<div class="abs social"><span></span><span></span><span></span><span></span></div>

</body>
</html>
```